Gardowell - Direct Mail DL flyer design

Create a direct market flyer (d/l size) to compel people to act and visit our website to buy life insurance.

Copy, example images and notes are provided

Target Market(s)

Families with debt who need life insurance

Industry/Entity Type

Insurance

Requirements
Must have
• Our logo
• Colours are Blue C99, M79, Y0, K0 Green C40, M0, Y100, K0
• Copy side 1 is "For the price of a coffee you can ensure you and your family get the right start."
• Copy side 2 is "It doesn't sound like much, but when it comes to life insurance, $1 a day* can make a huge difference if you were to die.
• For the cost of a cup of coffee a day, you can ensure your family will be left with enough to protect the home, pay for ongoing living expenses and fund your children's continued education.
• Your life is important
• Apply today and get 1 month free cover
• Build your tomorrow
• company logo gardowell.com.au make prominant
• *For a monthly premium of $25.33, a 35 year old non-smoking male can obtain $300,000 of term life cover.
• Example for illistration purpose only. The premium cited is current as at February 2016, is based on the factors referred to in the example and subject to underwriting. You should consider whether this product is appropriate for you. Refer to the Product Disclosure Statement, available from gardowell before deciding whether to acquire the product."
• Footer
• Gardowell Pty Ltd
• ABN 47 253 918 604 AFS Licence 729140
Nice to have
• Coffee cup with pods/capsuals around it white background side 1 and coffee ring stain on reverse as watermark
• Trusafe has been awarded - Merrow Ratings - 2014 Kestrel Protection Honours for Term Cover
• Trusafe has been awarded - Merrow Ratings - 2015 Kestrel Protection Honours for Term Cover

```html
<!DOCTYPE html>
<html lang="en">
<head>
<meta charset="utf-8">
<title>Gardowell DL Flyer</title>
<link href="https://fonts.googleapis.com/css2?family=Lato:wght@300;400;700;900&family=Cabin+Condensed:wght@400;600;700&display=swap" rel="stylesheet">
<style>
  :root {
    --green: #86c440;
    --blue: #2b3190;
    --ink: #2a2f7e;
    --stain: #6e4a2c;
    --white: #ffffff;
    --page: #ffffff;
  }
  * { box-sizing: border-box; margin: 0; padding: 0; }
  html, body { width: 1200px; height: 1174px; overflow: hidden; background: var(--page); }
  body { position: relative; font-family: "Lato", sans-serif; }

  .flyer { position: absolute; top: 80px; width: 467px; height: 990px; background: var(--white); overflow: hidden; }
  .flyer--front { left: 78px; }
  .flyer--back { left: 642px; }

  .green-band { position: absolute; left: 0; top: 0; width: 100%; background: var(--green); }
  .flyer--front .green-band { height: 544px; }
  .flyer--back .green-band { height: 538px; }

  .photo-placeholder { position: absolute; }
  .coffee-photo { left: 27px; top: 40px; width: 384px; height: 384px; border-radius: 50%;
    background: radial-gradient(circle, #efdcc0 0%, #d4a06a 55%, #c48a50 100%); }
  .capsule-photo--blue { left: 18px; top: 516px; width: 136px; height: 136px; border-radius: 10px; background: #3b2fb0; }
  .capsule-photo--green { left: 0; top: 624px; width: 104px; height: 152px; border-radius: 10px; background: #7cc04a; }
  .capsule-photo--small { left: 62px; top: 340px; width: 52px; height: 52px; border-radius: 8px; background: #3b2fb0; }
  .stain-photo { left: 54px; top: 48px; width: 372px; height: 320px; border-radius: 50%;
    background: radial-gradient(ellipse, rgba(110,74,44,0.05) 0%, rgba(110,74,44,0.22) 100%); }

  .front-headline { position: absolute; right: 40px; top: 606px; text-align: right; font-weight: 700;
    font-size: 46px; line-height: 43px; letter-spacing: -0.5px; color: var(--green); }
  .front-headline .accent { color: var(--blue); }

  .brand { position: absolute; display: flex; align-items: flex-start; gap: 14px; }
  .flyer--front .brand { left: 50px; top: 872px; }
  .flyer--back .brand { left: 40px; top: 864px; }
  .brand-mark { width: 66px; height: 66px; background: var(--green); border-radius: 8px; flex: none; }
  .brand-text { display: flex; flex-direction: column; align-items: flex-end; }
  .brand-name { font-weight: 400; font-size: 39px; line-height: 44px; color: var(--blue); letter-spacing: 0.3px; }
  .brand-tagline { font-weight: 400; font-size: 14px; letter-spacing: 3.4px; color: var(--blue); margin-top: 2px; }

  .stain-copy { position: absolute; left: 100px; top: 62px; width: 330px; text-align: center; transform: rotate(8deg);
    font-weight: 900; font-size: 28px; line-height: 32px; color: var(--stain); white-space: nowrap; }
  .stain-copy sup { font-size: 17px; }

  .back-body { position: absolute; left: 20px; top: 376px; width: 440px; text-align: center;
    font-family: "Cabin Condensed", sans-serif; font-weight: 600; font-size: 20px; line-height: 21.6px; color: var(--white); white-space: nowrap; }
  .back-body .lead { padding-left: 80px; }
  .back-slogan { position: absolute; left: 0; width: 100%; top: 492px; text-align: center;
    font-family: "Cabin Condensed", sans-serif; font-weight: 700; font-size: 25px; color: var(--blue); }

  .offer { position: absolute; left: 0; width: 100%; top: 550px; text-align: center; font-weight: 900;
    font-size: 35px; line-height: 36px; color: var(--green); letter-spacing: -0.5px; }
  .offer .accent { color: var(--blue); }

  .footnote { position: absolute; left: 0; width: 100%; top: 630px; text-align: center; font-weight: 300;
    font-size: 14.5px; line-height: 16px; color: var(--ink); }

  .disclaimer { position: absolute; left: 37px; top: 672px; width: 292px; font-family: "Cabin Condensed", sans-serif;
    font-weight: 400; font-size: 16px; line-height: 18.4px; color: var(--ink); white-space: nowrap; }
  .disclaimer em { font-style: italic; }
  .disclaimer strong { font-weight: 700; }

  .award { position: absolute; left: 336px; width: 90px; height: 64px; border-radius: 50%; border: 3px solid var(--blue); }
  .award--2014 { top: 676px; }
  .award--2015 { top: 746px; }
  .award-bar { position: absolute; left: 342px; top: 818px; width: 80px; height: 10px; background: var(--blue); }

  .legal-footer { position: absolute; left: 0; width: 100%; top: 938px; text-align: center;
    font-size: 14px; line-height: 20px; letter-spacing: 2.2px; color: var(--blue); word-spacing: 2px; }
</style>
</head>
<body>

<section class="flyer flyer--front">
  <div class="green-band"></div>
  <div class="photo-placeholder coffee-photo" role="img" aria-label="Photo: top view of a latte with leaf latte art in a white cup"></div>
  <div class="photo-placeholder capsule-photo--blue" role="img" aria-label="Photo: purple coffee capsule"></div>
  <div class="photo-placeholder capsule-photo--green" role="img" aria-label="Photo: green coffee capsule"></div>
  <h1 class="front-headline">for the price<br>of <span class="accent">a coffee</span> you<br>can ensure you<br>and your family<br>get <span class="accent">the right start</span></h1>
  <div class="brand">
    <div class="brand-mark"></div>
    <div class="brand-text">
      <span class="brand-name">gardowell.com.au</span>
      <span class="brand-tagline">build your tomorrow</span>
    </div>
  </div>
</section>

<section class="flyer flyer--back">
  <div class="green-band"></div>
  <div class="photo-placeholder stain-photo" role="img" aria-label="Faint coffee ring stain"></div>
  <p class="stain-copy">it doesn't<br>sound like much,<br>but when it comes<br>to life insurance,<br>$1 A DAY<sup>*</sup>can<br>make a huge<br>difference if<br>you were<br>to die</p>
  <div class="photo-placeholder capsule-photo--small" role="img" aria-label="Photo: small purple coffee capsule"></div>
  <p class="back-body"><span class="lead">For the cost of a cup of coffee a day,</span><br>you can ensure your family will be left<br>with enough to protect the home, pay for<br>ongoing living expenses and fund your<br>children's continued education.</p>
  <p class="back-slogan">Your life is important. Build your tomorrow</p>

  <h2 class="offer">APPLY TODAY AND GET<br>1 MONTH <span class="accent">FREE COVER</span></h2>
  <p class="footnote">*For a monthly premium of $25.33, a 35 year old<br>non-smoking male can obtain $300,000 of term life cover.</p>
  <p class="disclaimer">Example for illustration purpose only.<br>The premium cited is current as at February<br>2016, is based on the factors referred to in<br>the example and subject to underwriting.<br>You should consider whether this product<br>is appropriate for you. Refer to the <em>Product</em><br><em>Disclosure Statement</em>, available from<br><strong>gardowell</strong> before deciding whether<br>to acquire the product.</p>
  <div class="award award--2014"></div>
  <div class="award award--2015"></div>
  <div class="award-bar"></div>

  <div class="brand">
    <div class="brand-mark"></div>
    <div class="brand-text">
      <span class="brand-name">gardowell.com.au</span>
      <span class="brand-tagline">build your tomorrow</span>
    </div>
  </div>
  <p class="legal-footer">Gardowell Pty Ltd &nbsp; ABN 47 253 918 604<br>AFS Licence 729140</p>
</section>

</body>
</html>
```